Create a memorable Stationary for Security Software Company

TalbrenQuay is the worldwide leader in securing the Internet. Making Internet communications and critical data secure, reliable and available everywhere has been and continues to be our ongoing vision. We are committed to staying focused on real customer needs and to developing new and innovative security solutions that redefine the security landscape.

Industry/Entity Type

Internet

Font styles to use
Serif
Sans Serif
Script

Colors
0792cd
33a6d7
85cae6

```html
<!DOCTYPE html>
<html lang="en">
<head>
<meta charset="utf-8">
<title>TalbrenQuay Business Card</title>
<link rel="stylesheet" href="https://fonts.googleapis.com/css2?family=Arimo:wght@400;700&display=swap">
<style>
  :root {
    --brand-deep: #0792cd;
    --brand-mid: #33a6d7;
    --brand-light: #85cae6;
    --card-top: #8fd0ec;
    --card-bottom: #74c0e3;
    --ink-dark: #0a6fa0;
    --ink-white: #f4fbff;
    --page: #e9ecef;
  }
  * { box-sizing: border-box; margin: 0; padding: 0; }
  html, body { width: 1200px; height: 950px; overflow: hidden; }
  body {
    background: var(--page);
    font-family: "Arimo", Arial, sans-serif;
    display: flex;
    flex-direction: column;
    align-items: center;
    justify-content: center;
    gap: 34px;
  }
  .card {
    position: relative;
    width: 760px;
    height: 434px;
    background: linear-gradient(160deg, var(--card-top), var(--card-bottom));
    box-shadow: 0 8px 24px rgba(0,0,0,0.18);
    overflow: hidden;
  }
  .card__sheen {
    position: absolute;
    top: 0; bottom: 0;
    left: 58%;
    width: 70px;
    background: linear-gradient(90deg, rgba(255,255,255,0), rgba(255,255,255,0.22), rgba(255,255,255,0));
  }
  .brand {
    position: absolute;
    display: flex;
    align-items: center;
    gap: 12px;
    color: var(--brand-deep);
    font-weight: 700;
  }
  .brand__dot {
    border-radius: 50%;
    background: var(--brand-mid);
    flex: none;
  }
  /* back */
  .card--back .brand {
    left: 50%; top: 40%;
    transform: translate(-50%, -50%);
    font-size: 46px;
  }
  .card--back .brand__dot { width: 40px; height: 40px; }
  .card--back .web {
    position: absolute;
    left: 0; right: 0;
    top: 64%;
    text-align: center;
    color: var(--brand-mid);
    font-size: 18px;
    letter-spacing: 4px;
  }
  /* front */
  .card--front .brand {
    right: 50px; top: 110px;
    font-size: 30px;
  }
  .card--front .brand__dot { width: 28px; height: 28px; }
  .person {
    position: absolute;
    left: 50px; top: 138px;
  }
  .person__name { font-size: 22px; font-weight: 700; color: var(--ink-dark); }
  .person__role { font-size: 16px; color: var(--ink-white); margin-top: 4px; }
  .divider {
    position: absolute;
    left: 50px; right: 50px;
    top: 210px;
    height: 1px;
    background: var(--brand-deep);
  }
  .contacts {
    position: absolute;
    left: 50px; top: 222px;
    list-style: none;
    color: var(--ink-white);
    font-size: 17px;
  }
  .contacts li { display: flex; align-items: center; gap: 10px; margin-bottom: 6px; }
  .contacts svg { width: 18px; height: 18px; fill: var(--ink-dark); flex: none; }
  .address {
    position: absolute;
    right: 50px; bottom: 44px;
    text-align: right;
    color: var(--ink-white);
    font-size: 17px;
    line-height: 1.5;
  }
</style>
</head>
<body>
  <section class="card card--back">
    <div class="card__sheen"></div>
    <div class="brand"><span class="brand__dot"></span>TalbrenQuay</div>
    <p class="web">www.talbrenquay.com</p>
  </section>

  <section class="card card--front">
    <div class="card__sheen"></div>
    <div class="person">
      <p class="person__name">Maren Holt</p>
      <p class="person__role">President</p>
    </div>
    <div class="brand"><span class="brand__dot"></span>TalbrenQuay</div>
    <div class="divider"></div>
    <ul class="contacts">
      <li>
        <svg viewBox="0 0 24 24" aria-hidden="true"><path d="M3 8c0-2 2-3 9-3s9 1 9 3v2h-5V8H8v2H3zM6 12h12l2 8H4z"/></svg>
        555 0142 7781
      </li>
      <li>
        <svg viewBox="0 0 24 24" aria-hidden="true"><path d="M6 3h10v5H6zM3 9h18v9h-3v3H6v-3H3zM8 15v4h8v-4z"/></svg>
        555 0198 4630
      </li>
      <li>
        <svg viewBox="0 0 24 24" aria-hidden="true"><path d="M2 5h20v14H2zM4 7l8 6 8-6z"/></svg>
        maren@talbrenquay.com
      </li>
    </ul>
    <address class="address" style="font-style:normal">
      4127 Harrow Lane<br>
      Cedar Vale, NY 10982<br>
      www.talbrenquay.com
    </address>
  </section>
</body>
</html>
```